Business card design for Bront Engineering Qavo

We need a new business card design along with all the necessary to place an order. The company is Bront Engineering Qavo and we recently updated our logo.

```html
<!DOCTYPE html>
<html lang="en">
<head>
<meta charset="utf-8">
<title>Bront Engineering Qavo – Business Card</title>
<link rel="stylesheet" href="https://fonts.googleapis.com/css2?family=Montserrat:wght@600&family=Open+Sans:wght@400;600&display=swap">
<style>
  :root {
    --stage: #e4e1dc;
    --card-white: #f4f4f4;
    --ink-black: #141414;
    --brand-yellow: #e2cf2c;
    --brand-grey: #8e8e8e;
    --text-light: #f2f2f2;
    --photo-dark: #10151b;
    --photo-mid: #2b3744;
  }
  html, body {
    margin: 0;
    padding: 0;
    width: 1200px;
    height: 917px;
    overflow: hidden;
    background: var(--stage);
  }
  .canvas {
    position: relative;
    width: 1200px;
    height: 917px;
  }
  .card {
    position: absolute;
    width: 540px;
    height: 310px;
    overflow: hidden;
    box-shadow: 0 10px 28px rgba(0,0,0,0.25);
  }
  .card-front {
    left: 50px;
    top: 150px;
    background: var(--card-white);
  }
  .card-back {
    left: 610px;
    top: 455px;
  }
  .front-shapes {
    position: absolute;
    inset: 0;
  }
  .wordmark {
    position: absolute;
    display: flex;
    align-items: center;
    gap: 10px;
    font-family: "Montserrat", sans-serif;
    font-weight: 600;
    letter-spacing: 0.06em;
    text-transform: uppercase;
    white-space: nowrap;
  }
  .wordmark-mark {
    width: 12px;
    height: 12px;
    background: var(--brand-yellow);
    flex: none;
  }
  .card-front .wordmark {
    left: 34px;
    top: 66px;
    font-size: 22px;
    color: var(--brand-grey);
  }
  .holder {
    position: absolute;
    left: 34px;
    top: 168px;
    height: 30px;
    display: flex;
    align-items: center;
    gap: 8px;
    font-family: "Open Sans", sans-serif;
    color: var(--text-light);
    font-size: 13px;
    white-space: nowrap;
  }
  .holder-name {
    font-weight: 600;
    text-transform: uppercase;
    letter-spacing: 0.02em;
  }
  .holder-divider {
    width: 1px;
    height: 16px;
    background: var(--text-light);
  }
  .contact {
    position: absolute;
    left: 34px;
    top: 212px;
    margin: 0;
    padding: 0;
    list-style: none;
    font-family: "Open Sans", sans-serif;
    font-size: 12px;
    line-height: 19px;
    color: var(--text-light);
    white-space: nowrap;
  }
  .contact li {
    display: flex;
    align-items: center;
    gap: 8px;
  }
  .contact .address {
    padding-left: 18px;
  }
  .contact svg {
    width: 10px;
    height: 10px;
    flex: none;
  }
  .back-photo {
    position: absolute;
    inset: 0;
    background: radial-gradient(ellipse at 35% 70%, var(--photo-mid) 0%, var(--photo-dark) 70%);
  }
  .card-back .wordmark {
    left: 50%;
    top: 50%;
    transform: translate(-50%, -50%);
    font-size: 24px;
    color: var(--text-light);
  }
</style>
</head>
<body>
<main class="canvas">

  <section class="card card-front" aria-label="Business card front">
    <svg class="front-shapes" viewBox="0 0 540 310" width="540" height="310" aria-hidden="true">
      <polygon points="0,168 352,168 336,198 0,198" fill="var(--brand-yellow)"/>
      <polygon points="0,198 336,198 280,310 0,310" fill="var(--ink-black)"/>
    </svg>

    <div class="wordmark">
      <span class="wordmark-mark" aria-hidden="true"></span>
      <span class="wordmark-name">Bront Engineering Qavo</span>
    </div>

    <div class="holder">
      <span class="holder-name">Dara K. Morlen</span>
      <span class="holder-divider" aria-hidden="true"></span>
      <span class="holder-role">Partner</span>
    </div>

    <ul class="contact">
      <li class="address">Suite 9, 48 Harbour Lane</li>
      <li class="address">Portvale QLD 4810</li>
      <li>
        <svg viewBox="0 0 10 10" aria-hidden="true"><rect x="0.75" y="0.75" width="8.5" height="8.5" fill="none" stroke="var(--brand-yellow)" stroke-width="1.5"/></svg>
        <span>0123 555 904</span>
      </li>
      <li>
        <svg viewBox="0 0 10 10" aria-hidden="true"><rect x="0" y="0" width="10" height="10" fill="var(--brand-yellow)"/><path d="M2 2 L8 8 M8 2 L2 8" stroke="var(--ink-black)" stroke-width="1.4"/></svg>
        <span>info@brontqavo.co</span>
      </li>
    </ul>
  </section>

  <section class="card card-back" aria-label="Business card back">
    <div class="back-photo" role="img" aria-label="Dark close-up photograph of industrial wiring and machinery"></div>
    <div class="wordmark">
      <span class="wordmark-mark" aria-hidden="true"></span>
      <span class="wordmark-name">Bront Engineering Qavo</span>
    </div>
  </section>

</main>
</body>
</html>
```